New Church Plant website for Brightvale Church

I would like a six page website designed that is clean and easy to navigate. The six pages will include (1) About Us (2) Home (3) Contact Us (4) Sermons (5) Donate (6) Ministries. There will be subcategories for each category as well. The color scheme can be found in the attached magazine of Brightvale. Much of the information found in the booklet will be used on the website. I would love to see a design that pops but still clean and easy to navigate. I have included a good deal of pictures for the creative. Please see the current website at brightvalechapel.example which is temporary as we are preparing for a launch. I would now like to create a long-term site.

Target Market(s)

People interested in Christian church

Number of Pages Required

5+ page

Font styles to use
Sans Serif

Colors
ffffff
f78f20

Requirements
Must have
• a site that pops but is clean and easy to navigate.

```html
<!DOCTYPE html>
<html lang="en">
<head>
<meta charset="utf-8">
<title>Brightvale Church</title>
<link href="https://fonts.googleapis.com/css2?family=Montserrat:ital,wght@0,500;0,600;0,700;0,800;1,600&family=Open+Sans:wght@400;600;700&display=swap" rel="stylesheet">
<style>
:root{
  --orange:#f78f20;
  --white:#ffffff;
  --ink:#1d1d1d;
  --text:#555555;
  --grey-bg:#f1f1f1;
  --footer:#1b1b1b;
}
*{margin:0;padding:0;box-sizing:border-box}
html,body{width:1200px;height:3372px;overflow:hidden}
body{position:relative;background:var(--white);font-family:'Open Sans',sans-serif;color:var(--text)}
.abs{position:absolute}
.heading{font-family:'Montserrat',sans-serif}

/* header */
.site-header{left:0;top:0;width:1200px;height:100px;background:var(--white);z-index:3}
.brand{left:40px;top:28px;display:flex;align-items:center;gap:10px}
.brand-dot{width:34px;height:34px;border-radius:50%;background:var(--orange)}
.brand-name{font-family:'Montserrat',sans-serif;font-weight:700;font-size:24px;color:var(--orange)}
.main-nav{left:420px;top:40px;display:flex;gap:26px;font-family:'Montserrat',sans-serif;font-weight:700;font-size:12px;color:var(--ink);letter-spacing:.5px}
.donate-btn{left:1000px;top:30px;width:136px;height:40px;background:var(--orange);color:var(--white);font-family:'Montserrat',sans-serif;font-weight:700;font-size:12px;display:flex;align-items:center;justify-content:center;letter-spacing:.5px}

/* hero */
.hero{left:0;top:100px;width:1200px;height:520px;background:linear-gradient(180deg,#2b2520 0%,#4a3a30 45%,#2a221d 100%)}
.hero-title{left:0;top:270px;width:1200px;text-align:center;color:var(--white);font-weight:800;font-size:46px;letter-spacing:1px}
.hero-sub{left:0;top:336px;width:1200px;text-align:center;color:var(--white);font-weight:600;font-size:26px;letter-spacing:.5px}
.hero-wave{left:0;top:470px;width:1200px;height:160px}

/* planter */
.planter-photo{left:160px;top:650px;width:340px;height:640px;background:linear-gradient(180deg,#3a3a3a 0%,#1c1c1c 55%,#4e5d78 100%);border-radius:150px 150px 0 0}
.intro-block{left:632px;top:700px;width:450px;height:120px;background:var(--orange);display:flex;align-items:center;padding-left:36px;gap:20px}
.intro-iam{font-family:'Montserrat',sans-serif;font-weight:600;font-size:44px;color:var(--white)}
.intro-name{background:var(--ink);padding:10px 20px 8px;color:var(--white)}
.intro-name b{display:block;font-family:'Montserrat',sans-serif;font-weight:800;font-size:40px;line-height:1}
.intro-name span{display:block;font-size:11px;letter-spacing:1px;margin-top:3px}
.bio{left:632px;top:840px;width:450px;font-size:13px;line-height:1.6}
.bio p+p{margin-top:12px}
.rule{left:632px;top:1020px;width:130px;height:3px;background:var(--orange)}
.edu-title{left:632px;top:1040px;font-weight:800;font-size:24px;color:var(--orange)}
.edu-list{left:632px;top:1088px;width:450px;list-style:none}
.edu-list li{margin-bottom:14px;font-size:13px;color:var(--text);line-height:1.35}
.edu-list b{display:block;font-family:'Montserrat',sans-serif;font-size:17px;color:var(--ink)}

/* keys */
.keys-bg{left:0;top:1290px;width:1200px;height:760px}
.keys-photo{left:760px;top:1340px;width:320px;height:440px;background:linear-gradient(180deg,#5a4636 0%,#2c2520 60%,#1a1a1a 100%);border:8px solid var(--white)}
.keys-title{left:110px;top:1530px;color:var(--white);font-weight:800;font-size:28px}
.keys-list{left:110px;top:1600px;width:600px;list-style:none;color:var(--white);font-size:17px}
.keys-list li{position:relative;padding-left:28px;margin-bottom:16px;line-height:1.35}
.keys-list li::before{content:"";position:absolute;left:0;top:7px;width:11px;height:11px;border-radius:50%;background:var(--white)}

/* community */
.community-photo{left:140px;top:2130px;width:380px;height:270px;background:linear-gradient(135deg,#8a5b3c 0%,#3b2a22 55%,#c67a3c 100%)}
.community-title{left:580px;top:2140px;font-weight:800;font-size:26px;color:var(--ink)}
.community-list{left:580px;top:2196px;width:500px;list-style:none;font-size:15px;color:var(--ink)}
.community-list li{position:relative;padding-left:26px;margin-bottom:10px;line-height:1.4}
.community-list li::before{content:"";position:absolute;left:0;top:6px;width:11px;height:11px;border-radius:50%;background:var(--ink)}
.community-list li.accent::before{background:var(--orange)}

/* pillars */
.pillars{left:0;top:2420px;width:1200px;height:620px;background:var(--grey-bg)}
.pillars-title{left:0;top:2450px;width:1200px;text-align:center;color:var(--orange);font-weight:800;font-size:24px}
.pillars-intro{left:170px;top:2492px;width:860px;text-align:center;font-size:13px;line-height:1.55;color:var(--text)}
.pillar{top:2620px;width:296px;height:370px;background:var(--white)}
.pillar-img{width:296px;height:180px;background:linear-gradient(180deg,#6a3b1c 0%,#b8742e 50%,#3a2418 100%)}
.pillar h3{font-family:'Montserrat',sans-serif;font-weight:800;font-size:30px;color:var(--orange);text-align:center;margin-top:22px}
.pillar p{font-size:13px;text-align:center;padding:8px 24px 0;color:var(--ink);line-height:1.5}
.values{list-style:none;padding:4px 0 0 70px;font-size:12px;font-weight:700;color:var(--ink)}
.values li{position:relative;padding-left:18px;margin-bottom:3px}
.values li::before{content:"";position:absolute;left:0;top:5px;width:8px;height:8px;border-radius:50%;background:var(--orange)}

/* footer */
.site-footer{left:0;top:3040px;width:1200px;height:332px;background:var(--footer)}
.foot-brand{left:150px;top:3080px;display:flex;align-items:center;gap:8px}
.foot-brand .brand-dot{width:26px;height:26px}
.foot-brand .brand-name{font-size:20px}
.foot-contact{left:150px;top:3130px;font-size:12px;color:#cfcfcf;line-height:1.9}
.news-title{left:400px;top:3090px;font-family:'Montserrat',sans-serif;font-weight:700;font-size:15px;color:var(--white)}
.news-form{left:400px;top:3124px;display:flex;gap:8px}
.news-input{width:150px;height:30px;background:var(--white);font-size:11px;color:#999;padding:8px 10px}
.news-btn{width:74px;height:30px;border:1px solid #ccc;color:var(--white);font-size:11px;display:flex;align-items:center;justify-content:center}
.social{left:430px;top:3180px;display:flex;gap:10px}
.social span{width:22px;height:22px;border-radius:50%;background:var(--white)}
.map{left:740px;top:3080px;width:270px;height:150px;background:linear-gradient(135deg,#e8e4dc,#cfd8c8)}
.copyright{left:150px;top:3330px;font-size:10px;color:#9a9a9a}
.foot-strip{left:0;top:3362px;width:1200px;height:10px;background:var(--orange)}
</style>
</head>
<body>

<header class="abs site-header">
  <div class="abs brand"><span class="brand-dot"></span><span class="brand-name">Brightvale</span></div>
  <nav class="abs main-nav"><span>HOME</span><span>ABOUT</span><span>SERMONS</span><span>DONATIONS</span><span>PHOTOS</span><span>CONTACT</span></nav>
  <div class="abs donate-btn">DONATE NOW</div>
</header>

<section class="abs hero" role="img" aria-label="Congregation worshipping with raised hands"></section>
<h1 class="abs hero-title heading">LAUNCHING APRIL 12, 2020</h1>
<p class="abs hero-sub heading">“A MULTI-ETHNIC CHURCH PLANTING CHURCH”</p>
<svg class="abs hero-wave" viewBox="0 0 1200 160" preserveAspectRatio="none">
  <path d="M0 90 C300 20 700 150 1200 40 L1200 160 L0 160Z" fill="#f78f20"/>
  <path d="M0 110 C320 50 720 170 1200 70 L1200 160 L0 160Z" fill="#ffffff"/>
</svg>

<div class="abs planter-photo" role="img" aria-label="Portrait of church planter Daniel Reyes"></div>
<div class="abs intro-block">
  <span class="intro-iam">I AM</span>
  <div class="intro-name"><b>DANIEL</b><span>CHURCH PLANTER</span></div>
</div>
<div class="abs bio">
  <p>Daniel Reyes was born and raised as a preacher's kid in the central city of Lakefront. As a youth, he wandered far from faith and found trouble early. After a life-changing encounter with grace, he gave his life to Jesus and later became an ordained minister in 2005.</p>
  <p>Daniel Reyes was born and raised as a preacher's kid in the central city of Lakefront. As a youth, he wandered far from faith and by</p>
</div>
<div class="abs rule"></div>
<h2 class="abs edu-title heading">EDUCATION</h2>
<ul class="abs edu-list">
  <li><b>B.A. in Business</b>from Lakeshore University</li>
  <li><b>M.A. in Christian Ministry</b>from Northfield Theological Seminary</li>
  <li><b>Ed. D in Organizational Leadership(ABD)</b>from Westridge University.</li>
</ul>

<svg class="abs keys-bg" viewBox="0 0 1200 760" preserveAspectRatio="none">
  <path d="M0 80 C350 0 800 100 1200 20 L1200 680 C800 760 400 640 0 720Z" fill="#f78f20"/>
</svg>
<div class="abs keys-photo" role="img" aria-label="Portrait of a ministry leader"></div>
<h2 class="abs keys-title heading">KEY TO SUCCESS</h2>
<ul class="abs keys-list">
  <li>Create new assessments best defining the characteristics needed for a central city church planter.</li>
  <li>Build strong central city church planting network.</li>
  <li>Create urban/suburban church planting partnerships.</li>
  <li>Plant churches that plant churches.</li>
  <li>Identify and equip indigenous central city church planters.</li>
  <li>Establish a contextualized funding model.</li>
</ul>

<div class="abs community-photo" role="img" aria-label="Pastor and his wife smiling together"></div>
<h2 class="abs community-title heading">COMMUNITY CONNECTION</h2>
<ul class="abs community-list">
  <li>Board member of Neighborhood Depot and partner in care.</li>
  <li>Board member of Cedar Ridge High School.</li>
  <li class="accent">Member of steering Council of Harbor Health care.</li>
  <li>Founder and president of Common Ground Builders, a neighborhood development organization.</li>
  <li class="accent">President of the Lakefront Declaration, a group of multi-ethnic pastors from the Southern Lakes region who stand as one in promoting racial unity within the body of Christ.</li>
</ul>

<section class="abs pillars"></section>
<h2 class="abs pillars-title heading">WHAT'S THE GIST BEHIND THE FOUR PILLARS</h2>
<p class="abs pillars-intro">The gist of our mission is to build our ministry in a way where we don't add another thing to the lives of our people but rather, we seek to be a part of what is already happening in the lives of those we serve. Therefore, we intend to embrace the local mission efforts that already exist in our community.</p>

<div class="abs pillar" style="left:140px">
  <div class="pillar-img" role="img" aria-label="Worship gathering in warm light"></div>
  <h3>MISSION</h3>
  <p>To be a gospel centered, multi-ethnic, church planting church built on the pillars of mission, faith, work, and economics.</p>
</div>
<div class="abs pillar" style="left:452px">
  <div class="pillar-img" role="img" aria-label="Congregation gathered in a sanctuary"></div>
  <h3>VISION</h3>
  <p>Flourishing People Planting Flourishing Churches.</p>
</div>
<div class="abs pillar" style="left:764px">
  <div class="pillar-img" role="img" aria-label="Church members in prayer"></div>
  <h3>CORE VALUES</h3>
  <ul class="values"><li>BIBLICALLY CENTERED</li><li>DIVERSITY</li><li>AUTHENTICITY</li><li>COURAGEABILITY</li></ul>
</div>

<footer class="abs site-footer"></footer>
<div class="abs foot-brand"><span class="brand-dot"></span><span class="brand-name">Brightvale</span></div>
<div class="abs foot-contact">
  1420 Harbor Way, Suite 12<br>Lakefront, WI 53000<br>(555) 014-2290<br>info@brightvalechapel.example
</div>
<div class="abs news-title">Newsletter</div>
<div class="abs news-form"><div class="news-input">Email Address</div><div class="news-btn">Subscribe</div></div>
<div class="abs social"><span></span><span></span><span></span></div>
<div class="abs map" role="img" aria-label="Map showing the church location"></div>
<div class="abs copyright">© Copyright 2020 Brightvale Church. All Rights Reserved.</div>
<div class="abs foot-strip"></div>

</body>
</html>
```